Striking new Advert required for Commercial Real Estate Agency

We need a a NEW newspaper advertisement for the marketing of a large commercial property (a Backpackers lodge)

Dimensions are to be width of 101mm and height of 100mm (10cms)

Our key design statement for this advert is clean, modern and minimalist design, with accents of 'HOT PINK' colour to remove it from looking too boring, perhaps in the area of the contact icons. The heirachy of the advert is outlined in the attached ADVERTISEMENT TEXT FILE.

Our company name is THE MERIDAL COLLECTIVE, and we want our brand to appear professional yet classy in it's design style (sort of like an advertising or design agency)

We have two logo options below, one more square in its layout (which we prefer) and the other more rectangular, which may be better suited for the layout. We are not adverse to the logo being reversed (white text on black), along with other key element areas such as the main advert heading and the "FOR SALE" part, and think this would be a good option.
There are two photos attached to be included in the advert.

We have attached an example of an old advert that we did, which we DID NOT LIKE, and which was for a smaller width than the one we need (it is only 65% of the width of this one). WE have also atached a file showing layout of some of our competitors adverts, which we dont think are too good either.

We are really open for ideas, but have time pressures, so please come back with any questions as soon as you can, if needed.

Thank you
Updates

Thank you for the great and diverse designs. There are a few standout options, but one style that we prefer most.

Target Market(s)

We are wanting this newspaper advertisement to attract interest from real estat e developers, investors and motel/lodge owners, along with other high nett worth individuals

Industry/Entity Type

Real Estate

Font styles to use
Serif
Sans Serif

Colors
1b1b1b
a54499
474747
fbfbfb

Requirements
Must have
• Clean modern look, predominantly monochromatic or black and white, with the hot pink accent somewhere, as mentioned above.
• All the contents of the TEXT provided, perhaps with additional space to add a little more if needed, Please advise if you think we dont have enough space for all of the TEXT
Should not have
• Script like fonts
• Cartoonish characters
• a 'cheap' look

```html
<!DOCTYPE html>
<html lang="en">
<head>
<meta charset="utf-8">
<title>For Sale – Mount Ashdown Land Grab</title>
<link href="https://fonts.googleapis.com/css2?family=Montserrat:wght@300;400;500;700;800;900&display=swap" rel="stylesheet">
<style>
  :root {
    --page: #ffffff;
    --ink-light: #fbfbfb;
    --charcoal: #474747;
    --deep: #1b1b1b;
    --accent: #a54499;
    --panel-top: #4a2d9a;
    --panel-mid: #6a2f9c;
    --panel-low: #5a2a78;
    --contact-bg: #2f1c3c;
    --rule: rgba(255,255,255,0.55);
  }
  * { margin: 0; padding: 0; box-sizing: border-box; }
  html, body { width: 1200px; height: 1200px; overflow: hidden; background: var(--page); }
  body { font-family: "Montserrat", Arial, sans-serif; color: var(--ink-light); position: relative; }

  .advert {
    position: absolute; left: 121px; top: 128px; width: 955px; height: 946px;
    box-shadow: 3px 3px 5px rgba(0,0,0,0.35);
    overflow: hidden;
  }
  .property-photo {
    position: absolute; left: 0; top: 0; width: 560px; height: 666px;
    background: linear-gradient(180deg, #5f8fd0 0%, #a9c4e6 30%, #e9ecef 45%, #d9dcd9 70%, #5f7a3a 88%, #3f5a26 100%);
  }
  .feature-panel {
    position: absolute; left: 560px; top: 0; width: 395px; height: 666px;
    background: linear-gradient(180deg, var(--panel-top) 0%, var(--panel-mid) 45%, var(--panel-low) 100%);
  }
  .feature-panel > * { position: absolute; }
  .headline {
    left: 30px; top: 62px; white-space: nowrap;
    font-weight: 900; font-size: 62px; letter-spacing: -0.5px; line-height: 1;
  }
  .subtitle {
    left: 22px; top: 148px; white-space: nowrap;
    font-weight: 300; font-size: 27px; letter-spacing: -0.6px; line-height: 1.2;
  }
  .subtitle-rule { left: 22px; top: 185px; width: 360px; height: 2px; background: var(--rule); }
  .pin-icon { left: 43px; top: 204px; width: 56px; height: 80px; }
  .address {
    left: 131px; top: 210px; white-space: nowrap;
    font-weight: 400; font-size: 22px; line-height: 26px;
  }
  .description {
    left: 23px; top: 314px; width: 358px;
    font-size: 14px; line-height: 20px; font-weight: 400; letter-spacing: -0.1px;
  }
  .key-details { list-style: none; }
  .key-details li { position: relative; padding-left: 14px; }
  .key-details li::before {
    content: ""; position: absolute; left: 2px; top: 8px; width: 5px; height: 5px;
    border-radius: 50%; background: var(--accent);
  }
  .tender { font-weight: 700; letter-spacing: 0.3px; }

  .brand-band {
    position: absolute; left: 0; top: 666px; width: 560px; height: 280px; background: var(--charcoal);
  }
  .brand-square {
    position: absolute; left: 67px; top: 56px; width: 142px; height: 144px;
    border: 6px solid var(--ink-light);
  }
  .brand-name {
    position: absolute; left: 259px; top: 58px; white-space: nowrap;
    font-weight: 400; font-size: 36px; line-height: 46px; letter-spacing: 1.5px;
  }

  .contact-band {
    position: absolute; left: 560px; top: 666px; width: 395px; height: 280px;
    background: var(--contact-bg);
  }
  .contact-band > * { position: absolute; left: 13px; white-space: nowrap; line-height: 1.2; }
  .contact-label { top: 30px; font-weight: 300; font-size: 23px; letter-spacing: 0.3px; }
  .agent-name { top: 60px; font-weight: 800; font-size: 23px; }
  .phone { font-weight: 400; font-size: 25px; display: flex; align-items: center; gap: 3px; }
  .phone svg { width: 18px; height: 22px; }
  .phone--office { top: 92px; }
  .phone--mobile { top: 130px; }
  .email { top: 166px; font-weight: 700; font-size: 19px; }
  .website { top: 196px; font-weight: 700; font-size: 19px; }
</style>
</head>
<body>
  <div class="advert">
    <div class="property-photo" role="img" aria-label="Photo of the two-storey white weatherboard lodge with balconies, bay window and garden shrubs under a blue sky"></div>

    <section class="feature-panel">
      <h1 class="headline">FOR SALE</h1>
      <h2 class="subtitle">Mount Ashdown Land Grab</h2>
      <div class="subtitle-rule"></div>

      <svg class="pin-icon" viewBox="0 0 56 80" aria-hidden="true">
        <path d="M28 4 C14 4 5 14 5 27 C5 44 28 66 28 66 C28 66 51 44 51 27 C51 14 42 4 28 4 Z" fill="none" stroke="#fbfbfb" stroke-width="5"/>
        <circle cx="28" cy="27" r="9" fill="none" stroke="#fbfbfb" stroke-width="5"/>
        <ellipse cx="28" cy="74" rx="11" ry="3" fill="none" stroke="#fbfbfb" stroke-width="3"/>
      </svg>
      <p class="address">Harlow’s Lodge,<br>42 Kestrel Street,<br>Mount Ashdown</p>

      <div class="description">
        <p>This Old Beauty has served many, and is now ripe for development. One of Mt Ashdown’s largest land areas, now offered with vacant possession, with key details being:</p>
        <ul class="key-details">
          <li>Large Land area of 2076m² with elevated sunny position and great outlook + access from Wren Street</li>
          <li>Existing Backpackers Lodge of 970m² providing multiple rooms with amenity areas</li>
          <li>Four adjacent sites also available, taking total land area to 4452m², an unprecedented Land</li>
        </ul>
        <p>Offering in this popular city fringe location</p>
        <p class="tender">Now Selling by Closed Tender</p>
      </div>
    </section>

    <section class="brand-band">
      <div class="brand-square"></div>
      <p class="brand-name">THE<br>MERIDAL<br>COLLECTIVE</p>
    </section>

    <section class="contact-band">
      <p class="contact-label">Contact the Sole Agent</p>
      <p class="agent-name">Dean Morrow</p>
      <p class="phone phone--office">
        <svg viewBox="0 0 18 22" aria-hidden="true"><path d="M5 2 L8 7 L6 9 C7 12 9 15 11 16 L13 14 L17 18 L14 21 C8 20 2 12 2 5 Z" fill="none" stroke="#fbfbfb" stroke-width="2" stroke-linejoin="round"/></svg>(04) 555 0142
      </p>
      <p class="phone phone--mobile">
        <svg viewBox="0 0 18 22" aria-hidden="true"><rect x="3" y="2" width="12" height="19" rx="2" fill="none" stroke="#fbfbfb" stroke-width="2"/><line x1="7" y1="17" x2="11" y2="17" stroke="#fbfbfb" stroke-width="1.5"/></svg>(021) 555 018
      </p>
      <p class="email">dean@meridalcollective.co.nz</p>
      <p class="website">www.meridalcollective.co.nz</p>
    </section>
  </div>
</body>
</html>
```